Divorce Lawyer print and ebook cover (Lanterns over the quiet harbor )

I need a front and back cover for my divorce and family law book. I already have a photo and title. The back cover photo is not necessary but can be interesting the Front-main cover is a must

Target Market(s)

Prospective client

Colors

Designer to choose colors to be used in the design.

Requirements
Must have
• Front photo by viewable.

```html
<!DOCTYPE html>
<html lang="en">
<head>
<meta charset="utf-8">
<title>Lanterns over the Quiet Harbor — Cover Wrap</title>
<link href="https://fonts.googleapis.com/css2?family=Cinzel:wght@400&family=EB+Garamond:wght@400&family=Great+Vibes&display=swap" rel="stylesheet">
<style>
  :root {
    --page-bg: #f1f1f1;
    --cover-black: #000000;
    --body-text: #f2f2f2;
    --paper-white: #ffffff;
    --gold-dark: #4a3620;
    --gold-mid: #8d6a3c;
    --gold-light: #e6d6a0;
    --silver: #b8b6b0;
    --ink: #0c0b09;
  }
  * { margin: 0; padding: 0; box-sizing: border-box; }
  html, body {
    width: 899px; height: 1200px; overflow: hidden;
    background: var(--page-bg);
  }
  .cover-wrap {
    position: absolute; left: 11px; top: 296px;
    width: 877px; height: 608px;
    background: var(--cover-black);
    box-shadow: 0 2px 8px rgba(0,0,0,.18);
  }

  /* Back cover */
  .back-cover {
    position: absolute; left: 0; top: 0; width: 406px; height: 608px;
  }
  .back-copy {
    position: absolute; left: 37px; width: 322px;
    font-family: "EB Garamond", serif;
    font-size: 10.6px; line-height: 13.6px;
    color: var(--body-text); text-align: justify;
  }
  .back-copy--intro { top: 64px; }
  .back-copy--detail { top: 197px; }
  .back-copy--beside { left: 158px; top: 326px; width: 202px; }
  .author-photo-slot {
    position: absolute; left: 35px; top: 329px; width: 111px; height: 113px;
    background: var(--paper-white);
  }
  .code-slot {
    position: absolute; left: 253px; top: 510px; width: 111px; height: 64px;
    background: var(--paper-white);
  }

  /* Spine */
  .spine {
    position: absolute; left: 406px; top: 0; width: 65px; height: 608px;
    background: linear-gradient(180deg, #2a2016 0%, #5a4326 40%, #7d6540 75%, #a8956a 100%);
    display: flex; flex-direction: column; align-items: center;
  }
  .spine-text {
    writing-mode: vertical-rl; transform: rotate(180deg);
    font-family: "Cinzel", serif; color: var(--gold-light);
    white-space: nowrap;
  }
  .spine-title { position: absolute; top: 36px; height: 320px; font-size: 15px; display: flex; align-items: center; justify-content: center; }
  .spine-title .script { font-family: "Great Vibes", cursive; font-size: 20px; margin: 4px 0; }
  .spine-author { position: absolute; top: 398px; height: 152px; font-size: 16px; color: var(--ink); display: flex; align-items: center; }

  /* Front cover */
  .front-cover {
    position: absolute; left: 471px; top: 0; width: 406px; height: 608px;
  }
  .cover-photo {
    position: absolute; left: 0; top: 0; width: 406px; height: 316px;
    background:
      radial-gradient(ellipse 55% 45% at 62% 22%, rgba(255,236,170,.95) 0%, rgba(214,188,110,.6) 40%, rgba(120,130,90,0) 75%),
      radial-gradient(ellipse 40% 40% at 92% 70%, rgba(170,180,60,.7) 0%, rgba(120,140,60,0) 70%),
      linear-gradient(180deg, #5b6a5c 0%, #3d4f55 45%, #1e2c38 80%, #000 100%);
  }
  .front-title {
    position: absolute; left: 0; top: 328px; width: 406px;
    text-align: center; font-family: "Cinzel", serif;
  }
  .gold-text {
    background: linear-gradient(90deg, var(--gold-dark) 0%, var(--gold-mid) 25%, var(--silver) 50%, var(--gold-mid) 70%, var(--gold-light) 100%);
    -webkit-background-clip: text; background-clip: text; color: transparent;
  }
  .title-line-1 { font-size: 48px; line-height: 56px; letter-spacing: 1px; }
  .title-connector {
    display: flex; align-items: center; justify-content: center; gap: 10px;
    height: 40px;
  }
  .title-connector .rule { width: 76px; height: 3px; background: linear-gradient(90deg, var(--gold-dark), var(--gold-mid)); }
  .title-connector .rule:last-child { background: linear-gradient(90deg, var(--gold-mid), var(--gold-light)); }
  .title-connector .script {
    font-family: "Great Vibes", cursive; font-size: 44px; line-height: 40px;
    color: var(--gold-mid);
  }
  .title-line-2 { font-size: 37px; line-height: 64px; }
  .author-band {
    position: absolute; left: 0; top: 546px; width: 406px; height: 62px;
    background: linear-gradient(90deg, #6b5030 0%, #9a7c4c 25%, #b9b3a2 45%, #d9cd9c 70%, #efe7c2 100%);
    display: flex; align-items: center; justify-content: center;
    font-family: "Cinzel", serif; font-size: 36px; color: var(--ink);
  }
</style>
</head>
<body>
  <div class="cover-wrap">
    <section class="back-cover">
      <p class="back-copy back-copy--intro">Lorem ipsum dolor sit amet, consectetur adipiscing elit. Integer est sapien, laoreet finibus nulla eu, fermentum mollis orci. Nunc quis mi ac ex sodales lacinia ac ac nunc. Sed dolor augue, euismod aliquam eleifend vitae, lobortis eget arcu. Integer augue nunc, vestibulum eu augue id, ornare ornare tortor. Quisque sit amet dolor ornare arcu luctus vulputate at id sem. Nam ac massa sit amet orci efficitur consectetur. Nunc ullamcorper leo et magna tristique, in fringilla eros fringilla. Orci varius natoque penatibus et magnis dis parturient montes, nascetur ridiculus mus.</p>
      <p class="back-copy back-copy--detail">Vestibulum odio enim, fermentum ut leo id, viverra vehicula ligula. Quisque dapibus dolor purus, at consectetur ipsum fringilla sed. Pellentesque ultricies elit dignissim, convallis quam sed, facilisis augue. Donec congue sem a dolor tincidunt tempor. Quisque elit dolor, porta congue commodo nec, mattis sit amet dolor. Pellentesque tempor diam at quam ultricies rhoncus. Donec ultrices felis turpis, hendrerit commodo mauris rhoncus eu. Donec at scelerisque nibh. Fusce hendrerit sagittis semper.</p>
      <div class="author-photo-slot"></div>
      <p class="back-copy back-copy--beside">Lorem ipsum dolor sit amet, consectetur adipiscing elit. Integer est sapien, laoreet finibus nulla eu, fermentum mollis orci. Nunc quis mi ac ex sodales lacinia ac ac nunc. Sed dolor augue, euismod aliquam eleifend vitae, lobortis eget arcu. Integer augue nunc, vestibulum eu augue id, ornare ornare tortor. Quisque sit amet</p>
      <div class="code-slot"></div>
    </section>

    <section class="spine">
      <div class="spine-text spine-title"><span>LANTERNS&nbsp;</span><span class="script">over the</span><span>&nbsp;QUIET HARBOR</span></div>
      <div class="spine-text spine-author">AUTHOR NAME</div>
    </section>

    <section class="front-cover">
      <div class="cover-photo" role="img" aria-label="Cover photograph: a man in a dark suit stands at a fork in a misty forest road beneath a two-way signpost, warm golden light glowing through the trees"></div>
      <h1 class="front-title">
        <div class="title-line-1 gold-text">LANTERNS</div>
        <div class="title-connector"><span class="rule"></span><span class="script">over the</span><span class="rule"></span></div>
        <div class="title-line-2 gold-text">QUIET HARBOR</div>
      </h1>
      <div class="author-band">AUTHOR NAME</div>
    </section>
  </div>
</body>
</html>
```